Flyer design for retail store owners

i would need to have a flyer design for my retail shop customers to show that I am a mailbox store that has all major shipping vendors to for their shipping needs. Ensuring that they can take advantage of opening a house account at the store and billed monthly, word document has all the details. Please use stock images for the notary public, passport photos, mailbox brass pictures of my actual mailboxes are listed in the pictures. I need to make it POP and WOW these retail store owners as I am using it to advertise the business

```html
<!DOCTYPE html>
<html lang="en">
<head>
<meta charset="utf-8">
<title>Mailbox Rental Flyer</title>
<link href="https://fonts.googleapis.com/css2?family=Roboto+Condensed:wght@700&family=Lato:ital,wght@0,400;0,700;1,400;1,700&display=swap" rel="stylesheet">
<style>
  :root {
    --orange: #f7941d;
    --orange-deep: #ef5a24;
    --navy: #2b2a6b;
    --white: #ffffff;
    --paper: #f2f3f5;
    --stage: #a3a4a8;
    --brass-light: #e3c08a;
    --brass-dark: #9a6a2a;
  }
  * { margin: 0; padding: 0; box-sizing: border-box; }
  html, body { width: 1200px; height: 784px; overflow: hidden; }
  body { background: var(--stage); position: relative; font-family: "Lato", sans-serif; }

  .page {
    position: absolute; top: 106px; width: 442px; height: 572px;
    background: var(--white); overflow: hidden;
    box-shadow: 0 10px 30px rgba(0,0,0,.35);
  }
  .page--front { left: 144px; }
  .page--back { left: 615px; }
  .page svg.shapes { position: absolute; inset: 0; }

  .photo { position: absolute; }

  /* front */
  .cabinet-photo {
    left: 235px; top: 23px; width: 193px; height: 220px;
    background: linear-gradient(135deg, var(--brass-light), #c9995a 55%, var(--brass-dark));
  }
  .headline {
    position: absolute; left: 22px; top: 160px;
    font-family: "Roboto Condensed", sans-serif; font-weight: 700;
    color: var(--white); font-size: 56px; line-height: 50px; letter-spacing: -0.5px;
  }
  .intro {
    position: absolute; left: 22px; top: 282px; width: 284px;
    color: var(--white); font-size: 10.6px; line-height: 13px;
  }
  .promo-badge {
    position: absolute; left: 313px; top: 303px; width: 114px; height: 114px;
    border-radius: 50%; background: var(--orange-deep);
    border: 6px solid var(--navy); box-shadow: 0 0 0 3px var(--white) inset;
    color: var(--white); text-align: center; font-style: italic;
    display: flex; flex-direction: column; justify-content: center;
  }
  .promo-badge .tag { font-size: 7.5px; line-height: 8px; }
  .promo-badge .price { font-weight: 700; font-size: 40px; line-height: 42px; }
  .promo-badge .term { font-size: 7px; line-height: 7.5px; font-weight: 700; }
  .mailbox-wall {
    left: 0; top: 441px; width: 442px; height: 131px;
    background: linear-gradient(180deg, #f4ece0, #efe5d6 50%, #f7f2ea);
  }
  .offer-banner {
    position: absolute; left: 207px; top: 432px; width: 235px; height: 24px;
    background: var(--navy);
    clip-path: polygon(24px 0, 100% 0, 100% 100%, 0 100%);
    color: var(--white); font-style: italic; font-size: 9px; line-height: 24px;
    text-align: right; padding-right: 18px; z-index: 2;
  }
  .about {
    position: absolute; left: 18px; top: 481px; width: 406px;
    color: var(--navy); font-size: 8.3px; line-height: 10.3px; font-weight: 700;
  }

  /* back */
  .passport-photo {
    left: 47px; top: 34px; width: 134px; height: 134px; border-radius: 50%;
    background: linear-gradient(160deg, #f1f1f3, #c8c9cf);
  }
  .seal-photo {
    left: 0; top: 0; width: 442px; height: 572px;
    background: linear-gradient(135deg, #6b4a3c, #b48a78 45%, #e8e1d8 75%);
    clip-path: polygon(315px 4px, 442px 4px, 442px 232px, 370px 302px, 203px 112px);
  }
  .back-copy {
    position: absolute; left: 26px; top: 200px; width: 234px;
    color: var(--white); font-size: 8.3px; line-height: 10.4px;
  }
  .deals-title {
    position: absolute; left: 26px; top: 287px;
    color: var(--white); font-size: 9.5px; font-weight: 700;
  }
  .deals {
    position: absolute; left: 26px; top: 307px; width: 292px; list-style: none;
    color: var(--white); font-size: 8.3px; line-height: 10.4px;
  }
  .deals li { position: relative; padding-left: 15px; }
  .deals svg { position: absolute; left: 0; top: 1px; width: 9px; height: 9px; }
  .brass-wall {
    left: 0; top: 441px; width: 442px; height: 131px;
    background: linear-gradient(90deg, #7a5418, #c99a3a 30%, #8e6420 60%, #d8ac4e 85%, #6e4a14);
  }
</style>
</head>
<body>

<section class="page page--front">
  <svg class="shapes" width="442" height="572" viewBox="0 0 442 572">
    <defs>
      <linearGradient id="frontOrange" x1="0" y1="0" x2="0" y2="1">
        <stop offset="0" stop-color="#f7941d"/>
        <stop offset="1" stop-color="#ef5a24"/>
      </linearGradient>
    </defs>
    <rect width="442" height="441" fill="var(--paper)"/>
    <polygon points="0,110 110,0 300,0 442,150 442,441 0,441" fill="url(#frontOrange)"/>
    <polygon points="330,0 442,0 442,110 400,150" fill="var(--white)"/>
    <polygon points="0,115 60,58 70,72 0,140" fill="var(--navy)"/>
    <polygon points="300,280 442,140 442,175 318,298" fill="var(--white)" opacity=".9"/>
    <polygon points="308,400 380,330 400,350 330,420" fill="var(--navy)"/>
    <polygon points="170,100 200,130 272,190" fill="var(--navy)"/>
    <circle cx="138" cy="77" r="57" fill="var(--navy)"/>
    <circle cx="138" cy="77" r="50" fill="var(--white)"/>
  </svg>
  <div class="photo" role="img" aria-label="Close-up of an open brass mailbox door" style="left:91px;top:30px;width:94px;height:94px;border-radius:50%;background:radial-gradient(circle at 40% 40%, #6b4a22, #c99a58 70%, #e2c08a);"></div>
  <div class="photo cabinet-photo" role="img" aria-label="Brass mailbox cabinet with rows of small locking doors"></div>

  <h1 class="headline">Renting<br>a mail box</h1>
  <p class="intro">Renting a mail box is one of the most efficient and cost saving methods for receiving your mail and packages. Instead of having to worry about private security, weather conditions, sorting, and deliveries; all you have to do is pick-up your mail from our secured facility each day except Sundays.&nbsp; You will get a notification when mail arrives whether envelope or package, it will be scanned in daily which other mailbox stores do not offer! We offer onsite Notary Public with no appointments and onsite Passport Photos and can ship out same day.</p>

  <div class="promo-badge">
    <span class="tag">exclusive<br>promo deal!</span>
    <span class="price">$12</span>
    <span class="term">a month for 6-12<br>months leases!</span>
  </div>

  <div class="photo mailbox-wall" role="img" aria-label="Faded wall of post office mailboxes"></div>
  <p class="offer-banner">Take advantage of this limited time offer now!</p>
  <p class="about">At Swift Parcel &amp; Post, our goal is to make your shipping experience as convenient as possible. Whether you are shipping packages, documents, or packages, we are here to help. Whether you want to track your package or estimate the price of your package, it is easy for you. We are ready to handle all of your postal services! Get also the services you need; printing, copying, and stop in to purchase postage or shipping materials. Service point partners are SkyFreight, ParcelRun, National Post, and GlobeXpress.</p>
</section>

<section class="page page--back">
  <svg class="shapes" width="442" height="572" viewBox="0 0 442 572">
    <defs>
      <linearGradient id="backOrange" x1="0" y1="0" x2="0" y2="1">
        <stop offset="0" stop-color="#f7941d"/>
        <stop offset="1" stop-color="#ef5a24"/>
      </linearGradient>
    </defs>
    <rect width="442" height="441" fill="var(--paper)"/>
    <polygon points="0,60 58,0 442,0 442,441 0,441" fill="url(#backOrange)"/>
    <polygon points="0,120 100,20 110,32 0,140" fill="var(--white)"/>
    <polygon points="0,55 45,12 55,24 0,80" fill="var(--navy)"/>
    <polygon points="260,441 390,330 442,330 442,345 315,441" fill="var(--white)"/>
    <polygon points="258,441 400,330 410,330 420,345 300,441" fill="var(--navy)"/>
    <polygon points="203,112 315,4 442,4 442,232 370,302" fill="var(--white)" stroke="var(--white)" stroke-width="8" stroke-linejoin="round"/>
    <circle cx="114" cy="101" r="76" fill="var(--navy)"/>
  </svg>
  <div class="photo passport-photo" role="img" aria-label="Two passports with travel tickets"></div>
  <div class="photo seal-photo" role="img" aria-label="Wooden wax seal stamp beside a sealed scroll"></div>

  <p class="back-copy">Now renting mailboxes on Maple Ridge Commons Shopping Center. We are offering all Maple Ridge Commons shopping center owners/employees an exclusive promo deal! $12 a month for 6-12 months leases! You get a mailbox in the shop, a book of stamps(20 count), 3 notarizations by appointment, 100 copies of black and white, and 100 copies of color. Please see associate for sign up!</p>

  <h2 class="deals-title">CHECK OUT THESE OTHER DEALS!</h2>
  <ul class="deals">
    <li><svg viewBox="0 0 10 10"><circle cx="5" cy="5" r="4" fill="none" stroke="#fff" stroke-width="1"/><path d="M3 5 l1.6 1.6 L9 2" fill="none" stroke="#fff" stroke-width="1.3"/></svg>As a retail owner, you know how important it is to keep your customers coming back - you will get 20% discount for printing services.</li>
    <li><svg viewBox="0 0 10 10"><circle cx="5" cy="5" r="4" fill="none" stroke="#fff" stroke-width="1"/><path d="M3 5 l1.6 1.6 L9 2" fill="none" stroke="#fff" stroke-width="1.3"/></svg>We duplicate keys for $2/each, our regular price charge is $4/each. Save up to 50%!</li>
    <li><svg viewBox="0 0 10 10"><circle cx="5" cy="5" r="4" fill="none" stroke="#fff" stroke-width="1"/><path d="M3 5 l1.6 1.6 L9 2" fill="none" stroke="#fff" stroke-width="1.3"/></svg>Lamination is also discounted at 10% off.</li>
    <li><svg viewBox="0 0 10 10"><circle cx="5" cy="5" r="4" fill="none" stroke="#fff" stroke-width="1"/><path d="M3 5 l1.6 1.6 L9 2" fill="none" stroke="#fff" stroke-width="1.3"/></svg>10% off retail supplies ... must be minimum of 10$</li>
    <li><svg viewBox="0 0 10 10"><circle cx="5" cy="5" r="4" fill="none" stroke="#fff" stroke-width="1"/><path d="M3 5 l1.6 1.6 L9 2" fill="none" stroke="#fff" stroke-width="1.3"/></svg>For house accounts -a 5% discount will be deducted monthly of billing change to invoicing PLUS we're giving another 5% of the discount if you upgrade and sign up for mailbox. Great right?</li>
  </ul>

  <div class="photo brass-wall" role="img" aria-label="Close-up of a wall of brass post office boxes"></div>
</section>

</body>
</html>
```